Heat & air company needs eye catching van wrap for our fleet!

Need a van wrap designed for our fleet of vans. It should incorporate our logo, website address, phone number, license number (as it is on existing vans). Should use the blue and red from our logo as the primary colors. Should also mention plumbing under the logo in lighter blue. I really love the ice cubes on the bottom like the example I am attaching. I am attaching examples of existing and others I like from online. I do not want copies. I want unique and using imagination.

Industry/Entity Type

It Company

Requirements
Must have
• Logo very big. Use blue and red. Have license number same as existing van. Have plumbing under heating & Air Conditioning.

```html
<!DOCTYPE html>
<html lang="en">
<head>
<meta charset="UTF-8">
<title>Harlan Heating &amp; Air Conditioning – Fleet Wrap</title>
<link href="https://fonts.googleapis.com/css2?family=Open+Sans:wght@600;700;800&display=swap" rel="stylesheet">
<style>
  :root {
    --page: #ffffff;
    --wrap-white: #f4f6f8;
    --brand-red: #d91f1f;
    --brand-red-dark: #a81212;
    --brand-blue: #1a7ef0;
    --brand-blue-dark: #0b3fae;
    --ice-light: #e3ecf3;
    --ice-mid: #b9cad8;
    --ice-deep: #8ea6bb;
    --ink: #3a3a3a;
    --plumbing-blue: #5fb4ff;
    --name-grey: #4a4a4a;
  }
  * { box-sizing: border-box; margin: 0; padding: 0; }
  html, body {
    width: 1200px; height: 776px; overflow: hidden;
    background: var(--page);
    font-family: "Open Sans", Arial, sans-serif;
  }
  .canvas { position: relative; width: 1200px; height: 776px; }
  .wrap-panel {
    position: absolute; left: 50px; top: 168px;
    width: 1100px; height: 440px;
    border-radius: 18px; overflow: hidden;
    box-shadow: 0 10px 30px rgba(0,0,0,.12);
  }
  .wrap-art { position: absolute; inset: 0; display: block; }
  .phone {
    position: absolute; left: 262px; top: 190px;
    display: flex; align-items: center; gap: 8px;
    font-size: 27px; font-weight: 700; color: var(--ink);
    letter-spacing: 1px;
  }
  .phone svg { width: 18px; height: 28px; }
  .door-mark {
    position: absolute; left: 300px; top: 250px;
    width: 54px; height: 54px;
    background: var(--brand-blue-dark); border-radius: 6px;
  }
  .website {
    position: absolute; left: 420px; top: 372px;
    font-size: 24px; font-weight: 700; color: var(--ink);
  }
  .brand-lockup {
    position: absolute; left: 590px; top: 92px; width: 470px;
    text-align: center; color: var(--name-grey);
  }
  .brand-row { display: flex; align-items: center; gap: 14px; justify-content: center; }
  .brand-square {
    width: 52px; height: 52px; background: var(--name-grey); border-radius: 6px; flex: none;
  }
  .brand-name {
    font-size: 46px; font-weight: 800; letter-spacing: 2px; line-height: 1;
    color: var(--name-grey); text-align: left;
  }
  .brand-name small {
    display: block; font-size: 19px; letter-spacing: .5px; margin-top: 6px; font-weight: 800;
  }
  .service-line {
    margin-top: 8px; font-size: 17px; font-weight: 600;
    letter-spacing: 3px; color: var(--plumbing-blue);
  }
</style>
</head>
<body>
<main class="canvas">
  <section class="wrap-panel">
    <svg class="wrap-art" viewBox="0 0 1100 440" preserveAspectRatio="none">
      <defs>
        <linearGradient id="iceTone" x1="0" y1="0" x2="0" y2="1">
          <stop offset="0" stop-color="var(--wrap-white)"/>
          <stop offset=".35" stop-color="var(--ice-light)"/>
          <stop offset=".75" stop-color="var(--ice-mid)"/>
          <stop offset="1" stop-color="var(--ice-deep)"/>
        </linearGradient>
        <linearGradient id="blueTone" x1="0" y1="0" x2="0" y2="1">
          <stop offset="0" stop-color="var(--brand-blue)"/>
          <stop offset="1" stop-color="var(--brand-blue-dark)"/>
        </linearGradient>
        <linearGradient id="redTone" x1="0" y1="0" x2="1" y2="1">
          <stop offset="0" stop-color="var(--brand-red)"/>
          <stop offset="1" stop-color="var(--brand-red-dark)"/>
        </linearGradient>
      </defs>
      <rect class="base-white" width="1100" height="440" fill="var(--wrap-white)"/>
      <rect class="ice-field" role="img" aria-label="Photograph of clear ice cubes piled along the lower body" x="0" y="110" width="1100" height="330" fill="url(#iceTone)"/>
      <path class="red-sweep" d="M0 0 H150 C200 160 210 300 260 440 H0 Z" fill="url(#redTone)"/>
      <path class="blue-sweep" d="M520 0 H1100 V440 H670 C570 330 520 180 520 0 Z" fill="url(#blueTone)"/>
    </svg>

    <div class="phone">
      <svg viewBox="0 0 18 28" aria-hidden="true">
        <rect x="1.5" y="1.5" width="15" height="25" rx="3" fill="none" stroke="var(--ink)" stroke-width="2.5"/>
        <rect x="6" y="22" width="6" height="2" fill="var(--ink)"/>
      </svg>
      <span>405 555 0182</span>
    </div>
    <div class="door-mark" aria-hidden="true"></div>
    <div class="website">harlanair.com</div>

    <div class="brand-lockup">
      <div class="brand-row">
        <span class="brand-square" aria-hidden="true"></span>
        <p class="brand-name">HARLAN<small>HEATING &amp; AIR CONDITIONING</small></p>
      </div>
      <p class="service-line">- Plumbing -</p>
    </div>
  </section>
</main>
</body>
</html>
```